Marrowfield Benefit Advisors Business Card Design

I already placed order for cards through sketch hive.

Double sided- back Navy with White logo and raised silver "swoosh"

```html
<!DOCTYPE html>
<html lang="en">
<head>
<meta charset="UTF-8">
<title>Marrowfield Benefit Advisors – Business Card</title>
<link rel="stylesheet" href="https://fonts.googleapis.com/css2?family=Montserrat:wght@400;500;700&display=swap">
<style>
  :root {
    --bg: #1e1e20;
    --navy: #16275e;
    --navy-deep: #0f1c47;
    --navy-light: #22387f;
    --white: #ffffff;
    --text-navy: #1b2a5c;
    --text-grey: #3a3f4f;
    --rule: #8b90a0;
  }
  * { box-sizing: border-box; margin: 0; padding: 0; }
  html, body {
    width: 1200px; height: 801px; overflow: hidden;
    background: var(--bg);
    font-family: "Montserrat", sans-serif;
  }
  .stage {
    position: relative; width: 1200px; height: 801px;
    display: flex; align-items: center; justify-content: center; gap: 60px;
  }
  .card {
    width: 525px; height: 300px; border-radius: 18px;
    position: relative; overflow: hidden;
    box-shadow: 0 18px 40px rgba(0,0,0,0.55);
  }
  /* Front */
  .card-front { background: var(--white); display: flex; align-items: center; }
  .brand-block {
    width: 250px; display: flex; flex-direction: column; align-items: center;
  }
  .brand-name {
    font-weight: 700; font-size: 24px; color: var(--text-navy); letter-spacing: 0.5px;
  }
  .brand-tagline {
    font-weight: 500; font-size: 8px; letter-spacing: 3px; color: var(--text-navy);
    text-transform: uppercase; margin-top: 4px;
  }
  .divider { width: 1px; height: 150px; background: var(--rule); }
  .contact-block { padding-left: 22px; color: var(--text-grey); }
  .person-name { font-weight: 700; font-size: 22px; color: var(--text-navy); }
  .person-role { font-size: 12px; margin-top: 2px; }
  .address { font-size: 12px; line-height: 1.35; margin-top: 10px; }
  .contact-list { list-style: none; margin-top: 8px; font-size: 12px; }
  .contact-list li { display: flex; align-items: center; gap: 7px; line-height: 1.7; }
  .contact-list svg { width: 12px; height: 12px; flex: none; }
  .edge-band {
    position: absolute; left: 0; right: 0; bottom: 0; height: 8px; background: var(--navy);
  }
  /* Back */
  .card-back {
    background: linear-gradient(135deg, var(--navy-light) 0%, var(--navy) 45%, var(--navy-deep) 100%);
  }
  .back-texture {
    position: absolute; inset: 0;
    background: linear-gradient(160deg, rgba(255,255,255,0.05), rgba(0,0,0,0.12));
  }
  .back-brand {
    position: absolute; right: 70px; bottom: 80px;
    display: flex; align-items: center; gap: 10px;
  }
  .back-brand .dot { width: 12px; height: 12px; border-radius: 50%; background: #c9ccd4; }
  .back-brand .brand-name { color: var(--white); font-size: 30px; }
</style>
</head>
<body>
<main class="stage">
  <section class="card card-front" aria-label="Card front">
    <div class="brand-block">
      <span class="brand-name">Marrowfield</span>
      <span class="brand-tagline">Benefit Advisors</span>
    </div>
    <div class="divider"></div>
    <div class="contact-block">
      <h1 class="person-name">Leon Harwick</h1>
      <p class="person-role">Owner</p>
      <p class="address">48 Quarry Lane<br>Fenwick, NJ 07100 USA</p>
      <ul class="contact-list">
        <li>
          <svg viewBox="0 0 12 12" aria-hidden="true"><circle cx="6" cy="6" r="6" fill="var(--text-navy)"/><path d="M4 3.2c.3-.2.6 0 .7.3l.3.8c.1.2 0 .4-.2.6l-.3.3c.3.7.9 1.3 1.6 1.6l.3-.3c.2-.2.4-.2.6-.2l.8.3c.3.1.4.4.3.7l-.3.6c-2.6.2-4.6-1.8-4.4-4.4z" fill="#fff"/></svg>
          (555) 014-2270
        </li>
        <li>
          <svg viewBox="0 0 12 12" aria-hidden="true"><rect x="0.5" y="2" width="11" height="8" rx="1" fill="var(--text-navy)"/><path d="M1 2.6 6 6.5l5-3.9" stroke="#fff" stroke-width="0.9" fill="none"/></svg>
          info@marrowfield.com
        </li>
        <li>
          <svg viewBox="0 0 12 12" aria-hidden="true"><circle cx="6" cy="6" r="6" fill="var(--text-navy)"/><path d="M1 6h10M6 1c2 2.8 2 7.2 0 10M6 1c-2 2.8-2 7.2 0 10" stroke="#fff" stroke-width="0.8" fill="none"/></svg>
          www.marrowfield.com
        </li>
      </ul>
    </div>
    <div class="edge-band"></div>
  </section>

  <section class="card card-back" aria-label="Card back">
    <div class="back-texture" role="img" aria-label="Navy tone-on-tone backdrop"></div>
    <div class="back-brand">
      <span class="dot"></span>
      <span class="brand-name">Marrowfield</span>
    </div>
  </section>
</main>
</body>
</html>
```